Harborline Stay Collective Business Card Design

Design a business card for Harborline Stay Collective. Look at the website for colors and reference. Card should have logo, name, title, office number, mobile number, email, URL and a tagline like, "Luxury Hotel & Resort Email Marketing" (This might change).

https://www.harborlinestaycollective.net

The rest I will leave up to your imagination.

Contact Information for Business Card

Logo, name, title, office number, mobile number, email, URL and a tagline like, "Luxury Hotel & Resort Email Marketing" (This might change).

```html
<!DOCTYPE html>
<html lang="en">
<head>
<meta charset="utf-8">
<title>Harborline Stay Collective Business Card</title>
<link href="https://fonts.googleapis.com/css2?family=Montserrat:wght@400;500;600;700&family=Kristi&display=swap" rel="stylesheet">
<style>
  :root {
    --backdrop: #e6e6e6;
    --card: #000000;
    --accent: #f47b20;
    --ink: #ffffff;
  }
  * { margin: 0; padding: 0; box-sizing: border-box; }
  html, body {
    width: 1200px; height: 1200px; overflow: hidden;
    background: var(--backdrop);
    font-family: "Montserrat", Arial, sans-serif;
  }
  .sheet { position: relative; width: 1200px; height: 1200px; }
  .card {
    position: absolute; left: 156px; width: 888px; height: 520px;
    background: var(--card);
    box-shadow: 0 2px 6px rgba(0,0,0,0.25);
  }
  .card--front { top: 61px; }
  .card--back { top: 610px; }

  .brand {
    position: absolute; left: 0; right: 0;
    display: flex; align-items: center; justify-content: center; gap: 14px;
  }
  .brand__mark { width: 16px; height: 16px; background: var(--accent); }
  .brand__name {
    color: var(--ink); font-weight: 700; text-transform: uppercase;
    letter-spacing: 1px; white-space: nowrap;
  }
  .card--front .brand { top: 106px; }
  .card--front .brand__name { font-size: 33px; }
  .card--back .brand { top: 232px; }
  .card--back .brand__name { font-size: 40px; }
  .card--back .brand__mark { width: 20px; height: 20px; }

  .tagline {
    position: absolute; top: 198px; left: 0; right: 0; text-align: center;
    font-family: "Kristi", cursive; color: var(--ink); font-size: 44px;
  }
  .divider {
    position: absolute; top: 304px; left: 159px; width: 570px; height: 3px;
    background: var(--accent);
  }
  .person { position: absolute; left: 82px; top: 357px; }
  .person__name { color: var(--accent); font-size: 31px; font-weight: 600; line-height: 1.1; }
  .person__title { color: var(--ink); font-size: 19px; font-weight: 400; margin-top: 2px; }

  .contacts {
    position: absolute; right: 50px; top: 357px; list-style: none;
  }
  .contacts__item {
    display: flex; align-items: center; justify-content: flex-end; gap: 12px;
    height: 24.5px; color: var(--ink); font-size: 18.5px; font-weight: 400;
  }
  .contacts__icon { width: 12px; height: 12px; flex: none; }
  .contacts__domain { color: var(--accent); }
</style>
</head>
<body>
<main class="sheet">
  <section class="card card--front">
    <div class="brand">
      <span class="brand__mark"></span>
      <span class="brand__name">Harborline Stay Collective</span>
    </div>
    <p class="tagline">Luxury Hotel &amp; Resort Email Marketing</p>
    <div class="divider"></div>
    <div class="person">
      <p class="person__name">Daniel Reyes</p>
      <p class="person__title">Founder</p>
    </div>
    <ul class="contacts">
      <li class="contacts__item">033 4170 2286
        <svg class="contacts__icon" viewBox="0 0 12 12"><path fill="#f47b20" d="M2.3 0.6 4.2 2.5 3.3 4a7 7 0 0 0 4.7 4.7l1.5-.9 1.9 1.9-1.2 1.9C5 11.4.6 7 .4 1.8z"/></svg>
      </li>
      <li class="contacts__item">8561 904 317
        <svg class="contacts__icon" viewBox="0 0 12 12"><rect x="3" y="0.5" width="6" height="11" rx="1" fill="none" stroke="#f47b20" stroke-width="1.3"/><circle cx="6" cy="9.4" r="0.8" fill="#f47b20"/></svg>
      </li>
      <li class="contacts__item">info@harborlinestaycollective.net
        <svg class="contacts__icon" viewBox="0 0 12 12"><rect x="0.5" y="2" width="11" height="8" rx="1" fill="#f47b20"/><path d="M1 2.8 6 6.6l5-3.8" fill="none" stroke="#000" stroke-width="1"/></svg>
      </li>
      <li class="contacts__item"><span>www.<span class="contacts__domain">harborlinestaycollective</span>.net</span>
        <svg class="contacts__icon" viewBox="0 0 12 12"><g fill="none" stroke="#f47b20" stroke-width="1"><circle cx="6" cy="6" r="5.2"/><ellipse cx="6" cy="6" rx="2.3" ry="5.2"/><path d="M0.8 6h10.4M1.6 3.4h8.8M1.6 8.6h8.8"/></g></svg>
      </li>
    </ul>
  </section>

  <section class="card card--back">
    <div class="brand">
      <span class="brand__mark"></span>
      <span class="brand__name">Harborline Stay Collective</span>
    </div>
  </section>
</main>
</body>
</html>
```